Design some Business Cards

Will leave good review!
I need business cards with a logo and contact information.
This company name is 960 Plumbing Corp. Its a new Massachusetts plumbing business. 960 is phone area code in Massachusetts. Results have to look professional and clean. Please submit business card examples and logo ideas.
I was thinking 960 being designed as digits on the phone keys. Try to use a black background(with decorations or not), the rest being gold. Try to do a double sided design. Just large logo on one side, same slightly smaller logo and contact information on the other.

Lets go, we are getting there! I really like your ideas so far, thank you, I have more work to be done!
I will leave a 5 star review to the winner!

```html
<!DOCTYPE html>
<html lang="en">
<head>
<meta charset="utf-8">
<title>960 Plumbing Corp — Business Cards</title>
<link rel="stylesheet" href="https://fonts.googleapis.com/css2?family=Montserrat:wght@400;500;600&display=swap">
<style>
  :root {
    --backdrop: #2a2a2b;
    --card-black: #0b0b0b;
    --gold-light: #f0d878;
    --gold: #d4b04a;
    --gold-deep: #a98526;
    --ink-dark: #1a1408;
  }
  * { box-sizing: border-box; margin: 0; padding: 0; }
  html, body {
    width: 1200px; height: 800px; overflow: hidden;
    background: var(--backdrop);
    font-family: "Montserrat", Arial, sans-serif;
  }
  .stage {
    position: relative; width: 1200px; height: 800px;
    display: flex; align-items: center; justify-content: center; gap: 50px;
  }
  .card {
    position: relative; width: 540px; height: 309px; overflow: hidden;
    box-shadow: 0 10px 30px rgba(0,0,0,.45);
  }
  .gold-fill {
    background: linear-gradient(120deg, var(--gold-deep) 0%, var(--gold) 30%, var(--gold-light) 55%, var(--gold) 78%, var(--gold-deep) 100%);
  }
  .company-name {
    font-weight: 500; white-space: nowrap; letter-spacing: .3px;
  }

  /* Front side */
  .card-front { background: var(--card-black); }
  .card-front .company-name {
    position: absolute; left: 36px; top: 44px;
    color: var(--gold); font-size: 24px;
  }
  .contact {
    position: absolute; right: 40px; top: 160px; text-align: right; color: var(--gold);
  }
  .contact .person { font-size: 19px; font-weight: 600; letter-spacing: .2px; }
  .contact .phone {
    margin-top: 22px; font-size: 14px; font-weight: 400;
    display: flex; align-items: center; justify-content: flex-end; gap: 6px;
  }
  .footer-band {
    position: absolute; left: 0; right: 0; bottom: 0; height: 62px;
    display: flex; align-items: center; justify-content: center; gap: 6px;
    color: var(--ink-dark); font-size: 13px; font-weight: 500;
  }

  /* Back side */
  .card-back .company-name {
    position: absolute; left: 50%; top: 50%; transform: translate(-50%, -50%);
    color: var(--card-black); font-size: 30px;
  }
</style>
</head>
<body>
  <main class="stage">
    <section class="card card-front" aria-label="Front of business card">
      <p class="company-name">960 Plumbing Corp</p>
      <div class="contact">
        <p class="person">Dmitri Orlovsky</p>
        <p class="phone">(960) 555-0148
          <svg width="12" height="12" viewBox="0 0 24 24" aria-hidden="true">
            <path fill="currentColor" d="M6.6 10.8a15.1 15.1 0 0 0 6.6 6.6l2.2-2.2a1 1 0 0 1 1-.25 11.4 11.4 0 0 0 3.6.57 1 1 0 0 1 1 1V20a1 1 0 0 1-1 1A17 17 0 0 1 3 4a1 1 0 0 1 1-1h3.5a1 1 0 0 1 1 1c0 1.25.2 2.45.57 3.6a1 1 0 0 1-.25 1z"/>
          </svg>
        </p>
      </div>
      <div class="footer-band gold-fill">
        <svg width="13" height="13" viewBox="0 0 24 24" aria-hidden="true">
          <g fill="none" stroke="currentColor" stroke-width="2">
            <circle cx="12" cy="12" r="10"/>
            <ellipse cx="12" cy="12" rx="4.5" ry="10"/>
            <path d="M2 12h20M4 7h16M4 17h16"/>
          </g>
        </svg>
        <span>www.960plumbingco.com</span>
      </div>
    </section>

    <section class="card card-back gold-fill" aria-label="Back of business card">
      <p class="company-name">960 Plumbing Corp</p>
    </section>
  </main>
</body>
</html>
```